Website Refresh Needed - Large Couples Therapy Group

We are a large couples counselling group in Australia, and we have some key pages of our website that need refreshing, as it's a few years old now.
Similar colour palette as currently, and the same colours as the logo. No new logo required.
Total of 7 new (updated) page templates designs are needed:
1. HOME: https://www.velmoraclinic.com.au/
2: CONTACT US: https://www.velmoraclinic.com.au/contact/
3: RC CITY PAGE: https://www.velmoraclinic.com.au/city/sydney/
4: ST CITY PAGE: https://www.velmoraclinic.com.au/our-counselling/sex-therapy/sex-therapy-sydney/
5: ALL BLOGS: https://www.velmoraclinic.com.au/blog/
6: BLOG: https://www.velmoraclinic.com.au/sexual-desires-in-men-and-women-what-are-the-real-differences/
7: MAIN STANDARD PAGE: https://www.velmoraclinic.com.au/our-counselling/couples-relationship-counselling/

Target Market(s)

couples who are going through a crisis in their relationship or marriage.

Number of Pages Required

5+ page

Colors
86cfc6
b8a6cd
cfdfed

Requirements
Must have
• Calm, reassuring colours. People are stressed and need to know we can help.
Should not have
• No bright oranges or yellows.

```html
<!DOCTYPE html>
<html lang="en">
<head>
<meta charset="utf-8">
<title>Velmora Clinic – Relationship &amp; Marriage Counselling</title>
<link href="https://fonts.googleapis.com/css2?family=Montserrat:wght@300;400;500;600&family=Satisfy&display=swap" rel="stylesheet">
<style>
:root{
  --teal:#15808c;
  --teal-deep:#0f6f7a;
  --teal-card:#2a8f9b;
  --ink:#6f6f6f;
  --ink-soft:#9a9a9a;
  --heading:#7b7b7b;
  --grey-card:#6d6765;
  --panel:#f4f4f4;
  --rule:#d8d8d8;
  --white:#ffffff;
  --coral:#d9534f;
}
*{box-sizing:border-box;margin:0;padding:0}
html,body{width:1200px;height:5063px;overflow:hidden;background:var(--white)}
body{position:relative;font-family:'Montserrat',sans-serif;color:var(--ink)}
.abs{position:absolute}
.photo{position:absolute}
ul{list-style:none}

/* header */
.sidebar{left:0;top:0;width:322px;height:546px;background:var(--teal)}
.icon-btn{position:absolute;top:22px;width:32px;height:31px;border:1px solid rgba(255,255,255,.55)}
.icon-btn.menu{left:67px;background:rgba(255,255,255,.25)}
.icon-btn.search{left:104px;background:rgba(255,255,255,.12)}
.side-nav{position:absolute;left:65px;top:114px}
.side-nav li{height:43.2px;font-size:11px;color:var(--white);letter-spacing:.2px}
.side-nav .caret{font-size:8px;margin-left:5px}
.hero{left:322px;top:0;width:878px;height:546px;background:linear-gradient(135deg,#6e8aa2 0%,#c8b7a8 40%,#e8c6a4 65%,#9b8d80 100%)}
.logo{position:absolute;display:flex;align-items:center;gap:8px;font-size:19px;font-weight:400;color:var(--teal)}
.logo .dot{width:14px;height:14px;border-radius:50%;background:var(--teal)}
.hero .logo{left:246px;top:22px}
.hero-call{position:absolute;left:499px;top:32px;font-size:10px;font-weight:500;color:#3d3d3d;letter-spacing:.4px}
.hero-btn{position:absolute;left:628px;top:24px;width:183px;height:31px;background:rgba(200,200,200,.8);color:var(--white);font-size:8px;font-weight:600;letter-spacing:.8px;display:flex;align-items:center;justify-content:center}
.hero-caption{position:absolute;left:90px;top:508px;font-size:8px;font-weight:600;letter-spacing:3.2px;color:var(--white)}
.hero-count{position:absolute;left:705px;top:508px;font-size:8px;color:var(--white);letter-spacing:2px}
.hero-arrow{position:absolute;left:672px;top:266px}
.hero-diamond{position:absolute;left:708px;top:260px;width:26px;height:26px;background:rgba(150,150,150,.8);transform:rotate(45deg)}

/* intro */
.script-title{position:absolute;left:0;width:1200px;text-align:center;font-family:'Satisfy',cursive;color:var(--teal);font-size:31px}
.script-title span{border-bottom:1px solid var(--teal);padding-bottom:2px}
.intro-col{position:absolute;width:212px;font-size:10.5px;line-height:20px;color:var(--ink)}
.intro-col p+p{margin-top:14px}
.heart{position:absolute;color:var(--heading);font-size:11px}

/* gallery */
.gallery-band{left:0;top:1222px;width:1200px;height:80px;background:linear-gradient(180deg,#f4f4f4,#fff)}
.tile-label{position:absolute;left:110px;top:1380px;font-size:13px;font-weight:500;color:var(--white)}

/* therapists */
.section-title{position:absolute;left:0;width:1200px;text-align:center;font-size:24px;font-weight:300;color:var(--heading);letter-spacing:.5px}
.section-sub{position:absolute;left:0;width:1200px;text-align:center;font-size:14px;font-weight:300;color:var(--ink-soft)}
.panel{position:absolute;background:var(--panel)}
.play{position:absolute;width:48px;height:48px;border-radius:50%;background:var(--white);display:flex;align-items:center;justify-content:center}
.issue-list{position:absolute;font-size:10.5px;line-height:20px;color:var(--ink-soft)}
.issue-list li::before{content:"♥";font-size:6px;color:var(--heading);margin-right:6px;position:relative;top:-1px}
.rule-h{position:absolute;height:1px;background:var(--rule)}

/* about band */
.about{left:0;top:2538px;width:1200px;height:546px;background:linear-gradient(100deg,#2f3a2a 0%,#4b5643 35%,#8b8a80 55%,#3c4636 80%,#2a3226 100%)}
.about-title{position:absolute;left:0;top:2648px;width:1200px;text-align:center;font-size:25px;font-weight:400;color:var(--white);letter-spacing:.5px}
.about-quote{position:absolute;left:275px;top:2737px;width:650px;text-align:center;font-family:'Satisfy',cursive;font-size:20px;line-height:27px;color:var(--white)}
.learn{position:absolute;left:0;top:2950px;width:1200px;text-align:center;font-size:9px;color:var(--white);letter-spacing:1.6px}

/* feature cards */
.card-grey{position:absolute;background:var(--grey-card);color:var(--white);padding:40px 30px 0 32px}
.card-grey h3{font-size:16px;font-weight:600;letter-spacing:.8px;line-height:20px}
.card-grey p{font-size:13px;font-weight:300;line-height:20px;margin-top:14px}
.card-quote{position:absolute;left:737px;top:3176px;width:263px;height:385px;background:var(--teal-card);color:var(--white);padding:50px 30px 0 40px}
.card-quote .mark{font-family:Georgia,serif;font-size:52px;line-height:40px;font-weight:700}
.card-quote p{font-size:14px;font-style:italic;font-weight:300;line-height:24px;margin-top:8px}
.card-quote cite{display:block;margin-top:22px;font-style:normal;font-size:8px;letter-spacing:1px}

/* approach */
.approach-text{position:absolute;left:634px;top:3840px;width:310px;font-size:14px;font-weight:300;line-height:28px;color:var(--ink-soft)}

/* blog */
.blog-title{position:absolute;left:0;top:4218px;width:1200px;text-align:center;font-size:25px;font-weight:300;color:var(--heading);letter-spacing:1px}
.blog-title .news{color:#b8b8b8}
.post{position:absolute;top:4323px;width:150px}
.post .thumb{width:150px;height:191px}
.post .date{margin-top:12px;font-size:7px;letter-spacing:.5px;color:var(--ink)}
.post .date::before{content:"";display:inline-block;width:14px;height:1px;background:var(--rule);margin-right:6px;vertical-align:middle}
.post h4{margin:10px 0 0 20px;font-size:10px;font-weight:300;line-height:13px;color:var(--ink-soft)}

/* footer */
.footer-logo{left:522px;top:4790px}
.footer-links{position:absolute;left:0;top:4846px;width:1200px;text-align:center;font-size:7px;letter-spacing:.6px;color:var(--ink)}
.footer-links span{margin:0 5px}
.footer-copy{position:absolute;left:0;top:4866px;width:1200px;text-align:center;font-size:7px;letter-spacing:.6px;color:var(--ink)}
.social{position:absolute;top:4904px;display:flex;gap:4px;left:570px}
.social i{width:12px;height:12px;border:1px solid var(--ink-soft);border-radius:2px;display:block}
</style>
</head>
<body>

<!-- header -->
<aside class="abs sidebar">
  <div class="icon-btn menu"></div>
  <div class="icon-btn search"></div>
  <ul class="side-nav">
    <li>Home</li>
    <li>About us</li>
    <li>Counselling Types<span class="caret">♥</span></li>
    <li>Relationship Counseling Locations<span class="caret">♥</span></li>
    <li>Sex Therapy Locations<span class="caret">♥</span></li>
    <li>Quizzes<span class="caret">♥</span></li>
    <li>Fees &amp; Rebates<span class="caret">♥</span></li>
    <li>Faqs</li>
    <li>Contact us</li>
  </ul>
</aside>

<section class="abs hero" role="img" aria-label="Photo of a happy couple laughing together outdoors at sunset">
  <div class="logo"><span class="dot"></span>Velmora Clinic</div>
  <div class="hero-call">CALL : 1300 555 019</div>
  <div class="hero-btn">REQUEST AN APPOINTMENT</div>
  <svg class="hero-arrow" width="16" height="12" viewBox="0 0 16 12"><path d="M0 6h13M9 2l4 4-4 4" stroke="#555" stroke-width="1.3" fill="none"/></svg>
  <div class="hero-diamond"></div>
  <div class="hero-caption">EXPERT RELATIONSHIP &amp; MARRIAGE COUNSELLING</div>
  <div class="hero-count">1 / 4</div>
</section>

<!-- intro -->
<h1 class="script-title" style="top:608px"><span>We Specialise in Relationship &amp; Marriage Counselling</span></h1>

<div class="intro-col" style="left:200px;top:698px">
  <p>Welcome to the Velmora Clinic... You've come to the right place if you value your relationship, (along with being true to yourself) and would like help with how to repair the inevitable difficulties that come up in most relationships, and build a stronger more authentic connection.</p>
  <p>None of us, when we fall in love, imagine how difficult our relationship is going to be at times. We always hope for the best, then do our best, and still we can find that we can get stranded in problems that we don't really understand. We can unwittingly get into distressing lose-lose negative cycles, and not know how to get out of them.cycles, and not know how to get out of them.</p>
</div>
<div class="photo" style="left:456px;top:703px;width:288px;height:381px;background:linear-gradient(180deg,#dcd9d4,#c9b79f 55%,#a99b8f)" role="img" aria-label="Portrait of a smiling counsellor"></div>
<div class="intro-col" style="left:786px;top:698px">
  <p>This is perfectly understandable because most of us haven't been taught how to have a great relationship. We're just doing the best we know how.</p>
  <p>There is a very complex blend of science and art in creating great relationships, and this is both our passion and specialty.</p>
  <p>We're a group of nearly 100 psychologists, counsellors and sex therapists Australia wide who are passionate about relationships; understanding what makes them tick, how to best overcome difficulties, how to communicate effectively, how to get your relationship back on track, and even build new depths of compassion, understanding and honesty.</p>
</div>
<div class="heart" style="left:595px;top:1158px">♥</div>

<!-- gallery -->
<div class="abs gallery-band"></div>
<div class="photo" style="left:100px;top:1243px;width:385px;height:165px;background:linear-gradient(135deg,#3a2a3e,#a0524e 50%,#5a3a48)" role="img" aria-label="Couple dancing at a wedding reception"></div>
<div class="tile-label">Relationship Counselling</div>
<div class="photo" style="left:493px;top:1243px;width:212px;height:165px;background:linear-gradient(180deg,#c9d1cf,#8f9c98)" role="img" aria-label="Couple relaxing together in the sea"></div>
<div class="photo" style="left:713px;top:1243px;width:387px;height:165px;background:linear-gradient(180deg,#f3f3f3,#e6e6e6)" role="img" aria-label="Person lying curled on a white floor"></div>
<div class="photo" style="left:100px;top:1416px;width:605px;height:226px;background:linear-gradient(120deg,#3d3a40,#8a7a6a 45%,#c8b49a 60%,#454048)" role="img" aria-label="Newlyweds walking through guests throwing confetti"></div>
<div class="photo" style="left:713px;top:1416px;width:387px;height:226px;background:linear-gradient(180deg,#c9d8d0 0%,#8fae6e 55%,#6f9450)" role="img" aria-label="Two decorated wedding chairs on a lawn"></div>

<!-- therapists -->
<h2 class="section-title" style="top:1728px">OUR RELATIONSHIP THERAPISTS</h2>
<p class="section-sub" style="top:1770px">Can help with the following common relationship issues, and more</p>

<div class="panel" style="left:556px;top:1850px;width:444px;height:305px"></div>
<div class="photo" style="left:607px;top:1887px;width:346px;height:232px;background:linear-gradient(135deg,#8fb0c6,#d8c2a8 50%,#a88f7c)" role="img" aria-label="Couple embracing by the sea"></div>
<div class="play" style="left:756px;top:1979px"><svg width="14" height="16" viewBox="0 0 14 16"><path d="M2 1l11 7-11 7z" fill="var(--teal)"/></svg></div>
<ul class="issue-list" style="left:330px;top:1948px">
  <li>Affairs</li><li>Controlling behaviour</li><li>Verbal abuse</li><li>Imbalance of power</li><li>Lack of intimacy</li><li>Poor communication</li><li>Loss of love</li>
</ul>
<div class="rule-h" style="left:534px;top:1958px;width:49px"></div>

<div class="panel" style="left:200px;top:2157px;width:440px;height:300px"></div>
<div class="photo" style="left:249px;top:2192px;width:346px;height:232px;background:linear-gradient(135deg,#e4ddd6,#c7ab94 50%,#9d7f6d)" role="img" aria-label="Couple in a close embrace"></div>
<div class="play" style="left:398px;top:2284px"><svg width="14" height="16" viewBox="0 0 14 16"><path d="M2 1l11 7-11 7z" fill="var(--teal)"/></svg></div>
<ul class="issue-list" style="left:709px;top:2235px">
  <li>Relationship neglect</li><li>Sexual problems</li><li>Problems from childhood</li><li>Problems with parenting your children</li><li>Step children and in-laws</li><li>All forms of family problems</li><li>Anger management problems</li>
</ul>
<div class="rule-h" style="left:623px;top:2245px;width:49px"></div>

<!-- about -->
<section class="abs about" role="img" aria-label="Bride and groom holding hands among greenery"></section>
<h2 class="about-title">ABOUT THE VELMORA CLINIC</h2>
<p class="about-quote">Our vision is to be the most highly regarded and comprehensive marriage counselling, relationship counselling and sex therapy service in Australia, at reasonable and affordable rates. We hand choose our team of Registered Psychologists, Counsellors and Sex Therapists considering their knowledge, compassion, and unbiased approach to marriage counselling and sexual therapy and their experience in the relationship field.</p>
<div class="learn">LEARN &nbsp;♥&nbsp; MORE</div>

<!-- feature cards -->
<div class="photo" style="left:200px;top:3176px;width:262px;height:190px;background:linear-gradient(135deg,#efe7e0,#c9ad99 55%,#8c7060)" role="img" aria-label="Couple leaning in for a kiss"></div>
<div class="card-grey" style="left:200px;top:3366px;width:262px;height:195px">
  <h3>REBATES AVAILABLE</h3>
  <p>You may be able to receive rebates of up to 75% of your session costs.</p>
  <svg class="abs" style="left:178px;top:146px" width="50" height="30" viewBox="0 0 50 30"><path d="M2 12l10-8 9 5 8-5 10 3 9 6M12 4l-6 16M39 7l6 13M14 18l6 5 5-3 5 4 5-3" stroke="#fff" stroke-width="1.3" fill="none" stroke-linejoin="round"/></svg>
</div>
<div class="photo" style="left:469px;top:3176px;width:262px;height:190px;background:linear-gradient(180deg,#bcc6c9,#e4e2de 60%,#8d8478)" role="img" aria-label="Bride and groom seated on a sofa by the sea"></div>
<div class="card-grey" style="left:469px;top:3366px;width:262px;height:195px;padding-top:34px">
  <h3>SATISFACTION<br>GUARANTEE</h3>
  <p>We're proud to offer our 100% risk-free, satisfaction guarantee.</p>
  <svg class="abs" style="left:204px;top:24px" width="42" height="42" viewBox="0 0 42 42"><rect x="14" y="4" width="22" height="28" fill="none" stroke="#fff" stroke-width="1.3"/><path d="M19 12h12M19 18h12M2 24h8l6 4h10l-2 6H8l-6-4z" stroke="#fff" stroke-width="1.3" fill="none"/></svg>
</div>
<blockquote class="card-quote">
  <div class="mark">“</div>
  <p><strong>Connection</strong> is the energy between people when they feel seen, heard, and valued; when they can give and recieve without judgement; and when they get sustenance and strength from the relationship.</p>
  <cite>—— MAREN HOLT</cite>
</blockquote>

<!-- approach -->
<h2 class="section-title" style="top:3678px">OUR MARRIAGE COUNSELLING APPROACH</h2>
<div class="rule-h" style="left:582px;top:3751px;width:10px;background:var(--ink-soft)"></div>
<svg class="abs" style="left:122px;top:3922px" width="26" height="52" viewBox="0 0 26 52"><path d="M22 2L4 26l18 24" stroke="#9a9a9a" stroke-width="1.5" fill="none"/></svg>
<div class="photo" style="left:234px;top:3791px;width:343px;height:320px;background:linear-gradient(135deg,#e6ddd4,#c7a88f 50%,#6e5a4d)" role="img" aria-label="Couple touching foreheads and smiling"></div>
<p class="approach-text">It is very important to us that we take a very positive approach to relationship counselling. From your very first session, we will take the time to fully understand each of your individual perspectives, without bias, and get to the very root of the issues that are affecting your relationship.</p>
<svg class="abs" style="left:998px;top:3900px" width="26" height="52" viewBox="0 0 26 52"><path d="M4 2l18 24L4 50" stroke="#9a9a9a" stroke-width="1.5" fill="none"/></svg>

<!-- blog -->
<h2 class="blog-title">BLOGS &nbsp;/&nbsp; <span class="news">NEWS</span></h2>
<article class="post" style="left:134px"><div class="thumb" role="img" aria-label="Wedding couple portrait" style="background:linear-gradient(180deg,#d6cfc8,#5f5752)"></div><div class="date">30 AUG 2020</div><h4>What is Borderline Personality Disorder and how does it affect my</h4></article>
<article class="post" style="left:290px"><div class="thumb" role="img" aria-label="Couple posing in a city street" style="background:linear-gradient(180deg,#c4ccd2,#6d6a6a)"></div><div class="date">30 AUG 2020</div><h4>What is Borderline Personality Disorder and how does it affect my</h4></article>
<article class="post" style="left:447px"><div class="thumb" role="img" aria-label="Wedding celebration with confetti" style="background:linear-gradient(180deg,#5e4a54,#c99aa0)"></div><div class="date">30 AUG 2020</div><h4>What is Borderline Personality Disorder and how does it affect my</h4></article>
<article class="post" style="left:603px"><div class="thumb" role="img" aria-label="Black and white wedding kiss" style="background:linear-gradient(180deg,#cfcfcf,#3f3f3f)"></div><div class="date">30 AUG 2020</div><h4>What is Borderline Personality Disorder and how does it affect my</h4></article>
<article class="post" style="left:760px"><div class="thumb" role="img" aria-label="Outdoor wedding ceremony" style="background:linear-gradient(180deg,#dfe6e6,#8a9a86)"></div><div class="date">30 AUG 2020</div><h4>What is Borderline Personality Disorder and how does it affect my</h4></article>
<article class="post" style="left:917px"><div class="thumb" role="img" aria-label="Couple holding hands with bouquet" style="background:linear-gradient(180deg,#e8e6e2,#8aa08a)"></div><div class="date">30 AUG 2020</div><h4>What is Borderline Personality Disorder and how does it affect my</h4></article>

<!-- footer -->
<div class="logo abs footer-logo"><span class="dot"></span>Velmora Clinic</div>
<nav class="footer-links"><span>HOME</span><span>ABOUT US</span><span>OUR BLOGS</span><span>MEMBERS</span><span>LOG IN</span><span>CONTACT US</span></nav>
<div class="footer-copy">© COPYRIGHT 2020 &nbsp;//&nbsp; TERMS AND POLICY &nbsp;//&nbsp; WWW.VELMORACLINIC.COM.AU</div>
<div class="social"><i></i><i></i><i></i><i></i></div>

</body>
</html>
```